Website Design for Business Law Firm

We have a logo and now we would like a web site design for our new website. Our small firm provides creative and aggressive transactional (not litigation) legal services to advise healthcare, technology, internet-based and traditional companies and investors in such companies on healthcare, technology, financing, mergers/acquisitions, real estate and other transactions, legal compliance and general corporate and business matters.

We would like to see a website design that is professional and appropriate for executives, professionals, investors and government regulators to visit, that conveys professionalism and competence while being a little edgy and modern - no typical legal motifs such as gavels, books, or scales of justice. We advise businesses and investors and guide them through complicated issues quickly, capably and differently from other law firms. We are part of the business team and get things done.

The logo is attached, and we like gray as a color to complement it. The intention of the logo is to convey that in a storm or challenging time, people come to this firm, and people come to this firm when they need the power and disruption to change things or shake them up.

I have also enclosed a picture of our business card for consideration.

On the other hand, you can check out the current simple site at www.quenlow.example to see we have used a space motif in the past to evoke that we help create stars (the nebula featured there). This is not a necessary part of the new website and it may look better without it.

We appreciate your creativity and look forward to designs.

Industry/Entity Type

Business

Requirements
Must have
• We anticipate the following pages, and you may submit different ideas for the different pages:
• 1. Landing page
• 2. Services pages - healthcare, IT/Technology, general counsel services, financings, mergers/acquisitions, mediation/arbitration, procurement and productization
• 3. About Us including contact information
• Our name and contact information:
• Quenlow Law Firm, P.C.
• 7816 SW 19th Ave.
• Portland, OR 97213
• phone: 555.614.2873
• fax: 555.730.4158
Nice to have
• Please consider designs that enhance the impressions we are looking for
Should not have
• Please no gavels, scales of justice, law books, or similar traditional legal imagery.

```html
<!DOCTYPE html>
<html lang="en">
<head>
<meta charset="utf-8">
<title>Quenlow Law Firm</title>
<link href="https://fonts.googleapis.com/css2?family=Bebas+Neue&family=Open+Sans:wght@400;600;700&display=swap" rel="stylesheet">
<style>
:root{
  --hero-bg:#262626;
  --section-bg:#161616;
  --footer-bg:#232323;
  --teal:#4d6d72;
  --teal-line:#5b7d80;
  --nav-grey:#8c8c8c;
  --white:#ffffff;
  --text-light:#e6e6e6;
  --field-border:#cfcfcf;
  --button-dark:#262626;
  --dot-line:#3a3a3a;
}
*{margin:0;padding:0;box-sizing:border-box}
html,body{width:1035px;height:1200px;overflow:hidden;background:var(--section-bg)}
body{position:relative;font-family:"Open Sans",Arial,sans-serif;color:var(--text-light)}
.abs{position:absolute}
.bebas{font-family:"Bebas Neue",Impact,sans-serif;font-weight:400}

.hero{position:absolute;left:0;top:0;width:1035px;height:466px;background:radial-gradient(ellipse at 40% 50%,#2c2c2c 0%,var(--hero-bg) 70%)}
.top-rule{position:absolute;left:0;top:0;width:1035px;height:3px;background:var(--teal-line)}
.dotted{position:absolute;left:0;width:1035px;border-top:1px dashed var(--dot-line)}
.phone-line{display:flex;align-items:center;gap:8px}
.phone-icon{width:20px;height:20px;border-radius:50%;background:var(--teal);display:flex;align-items:center;justify-content:center}
.phone-number{font-size:25px;color:var(--white);letter-spacing:.3px}
.main-nav{left:186px;top:64px;display:flex;gap:16px;font-size:19px;letter-spacing:.3px}
.main-nav a{color:var(--nav-grey);text-decoration:none}
.main-nav a.current{color:var(--white)}
.portrait{left:588px;top:24px;width:304px;height:442px;background:linear-gradient(180deg,#3a3430 0%,#1d1d1f 35%,#151515 100%);border-radius:120px 120px 0 0}
.wordmark{left:184px;top:136px;width:250px;height:60px;display:flex;align-items:center;font-size:34px;font-weight:600;color:var(--white);letter-spacing:6px}
.headline{left:187px;top:217px;font-size:22px;font-weight:700;line-height:27px;letter-spacing:1.3px;color:var(--white)}
.service-list{font-size:12px;line-height:19.5px;color:#d4d4d4;list-style:none}
.service-list li{display:flex;align-items:center;gap:5px}
.cta{left:188px;top:365px;width:219px;height:51px;background:#0c0c0c;display:flex;align-items:center;justify-content:center;font-size:29px;color:var(--white);letter-spacing:.5px}
.learn-link{left:414px;top:401px;font-size:11px;letter-spacing:1px;color:#d8d8d8}

.section-title{color:var(--teal);letter-spacing:.2px}
.practices-photo{left:186px;top:578px;width:83px;height:146px;background:linear-gradient(160deg,#5a6a80 0%,#2c3446 60%,#20232c 100%)}
.practice-list{left:278px;top:579px;list-style:none;font-size:9.6px;line-height:13px;color:var(--white)}
.practice-list li::before{content:"› ";}
.btn{display:flex;align-items:center;justify-content:center;background:var(--teal);color:var(--white);font-size:9.5px;letter-spacing:.6px}
.contact-card{left:490px;top:510px;width:357px;height:223px;background:radial-gradient(ellipse at 40% 25%,#d9d9d9 0%,#ffffff 55%)}
.field{position:absolute;background:var(--white);border:1px solid var(--field-border);font-size:9.5px;color:#808080;padding:5px 6px}
.submit{left:602px;top:669px;width:148px;height:37px;background:var(--button-dark);color:var(--white);display:flex;align-items:center;justify-content:center;font-size:27px}

.body-copy{left:189px;top:867px;width:376px;font-size:9.8px;line-height:15.6px;color:var(--white)}
.news-thumb{width:43px;height:43px}
.news-date{font-size:11px;color:var(--teal-line)}
.news-text{font-size:10.5px;line-height:12.4px;color:var(--white)}

.footer{position:absolute;left:0;top:1048px;width:1035px;height:152px;background:var(--footer-bg)}
.footer-nav{position:absolute;left:0;width:1035px;top:34px;display:flex;justify-content:center;gap:14px;font-size:9.6px;color:var(--white)}
</style>
</head>
<body>

<header class="hero">
  <div class="top-rule"></div>
  <div class="dotted" style="top:57px"></div>
  <div class="dotted" style="top:97px"></div>

  <div class="portrait abs" role="img" aria-label="Photo of a smiling young businessman in a dark suit holding a rolled newspaper"></div>

  <div class="phone-line abs" style="left:714px;top:20px">
    <span class="phone-icon"><svg width="11" height="11" viewBox="0 0 12 12"><rect x="3" y="1" width="6" height="3" fill="#fff"/><rect x="1" y="4" width="10" height="5" rx="1" fill="#fff"/><rect x="3" y="7" width="6" height="4" fill="#fff" stroke="#4d6d72" stroke-width=".8"/></svg></span>
    <span class="phone-number bebas">555.730.4158</span>
  </div>

  <nav class="main-nav abs bebas">
    <a href="#">Home</a>
    <a href="#" class="current">Our Prectices</a>
    <a href="#">Professionals</a>
    <a href="#">Careers</a>
    <a href="#">About Us</a>
    <a href="#">Contact</a>
  </nav>

  <div class="wordmark abs">QUENLOW</div>

  <h1 class="headline abs">PRAGMATIC, CREATIVE SERVICES<br>FOR INNOVATIVE BUSINESSES</h1>

  <ul class="service-list abs" style="left:187px;top:279px">
    <li><svg width="10" height="10" viewBox="0 0 10 10"><circle cx="5" cy="5" r="4" fill="none" stroke="#d4d4d4"/><path d="M3 5l1.5 1.5L7 3.8" fill="none" stroke="#d4d4d4"/></svg>Strategic Alliances</li>
    <li><svg width="10" height="10" viewBox="0 0 10 10"><circle cx="5" cy="5" r="4" fill="none" stroke="#d4d4d4"/><path d="M3 5l1.5 1.5L7 3.8" fill="none" stroke="#d4d4d4"/></svg>Business Relationships</li>
    <li><svg width="10" height="10" viewBox="0 0 10 10"><circle cx="5" cy="5" r="4" fill="none" stroke="#d4d4d4"/><path d="M3 5l1.5 1.5L7 3.8" fill="none" stroke="#d4d4d4"/></svg>Outsourcing</li>
  </ul>
  <ul class="service-list abs" style="left:344px;top:279px">
    <li><svg width="10" height="10" viewBox="0 0 10 10"><circle cx="5" cy="5" r="4" fill="none" stroke="#d4d4d4"/><path d="M3 5l1.5 1.5L7 3.8" fill="none" stroke="#d4d4d4"/></svg>Procurements - Buying or Selling</li>
    <li><svg width="10" height="10" viewBox="0 0 10 10"><circle cx="5" cy="5" r="4" fill="none" stroke="#d4d4d4"/><path d="M3 5l1.5 1.5L7 3.8" fill="none" stroke="#d4d4d4"/></svg>Licensing and Technology Exploitation</li>
    <li><svg width="10" height="10" viewBox="0 0 10 10"><circle cx="5" cy="5" r="4" fill="none" stroke="#d4d4d4"/><path d="M3 5l1.5 1.5L7 3.8" fill="none" stroke="#d4d4d4"/></svg>Venture Formation and Startup</li>
  </ul>

  <div class="cta abs bebas">Call to Action</div>
  <div class="learn-link abs">Learn More &gt;&gt;</div>
</header>

<section class="practices">
  <h2 class="section-title bebas abs" style="left:182px;top:508px;font-size:33px">Our Practices Areas</h2>
  <p class="abs" style="left:186px;top:546px;font-size:11px;line-height:12.5px;color:#fff">Lorem ipsum dolor sit amet, consectetur adipiscing elit.<br>In fermen dolor tum dolor non augue pretium</p>
  <div class="practices-photo abs" role="img" aria-label="Photo of a businessman giving a thumbs up"></div>
  <ul class="practice-list abs">
    <li>Strategic Alliances</li>
    <li>Business Relationships</li>
    <li>Outsourcing</li>
    <li>Procurements - Buying or Selling</li>
    <li style="margin-top:2px">Licensing and Technology Exploitation</li>
    <li>Venture Formation and Startup</li>
    <li>Venture Financing</li>
    <li>Creative Private Financing Arrangements</li>
    <li>Mergers and Acquisitions</li>
    <li>Real Estate</li>
    <li>Contacts</li>
  </ul>
  <div class="btn abs" style="left:394px;top:719px;width:69px;height:15px">Learn More</div>
</section>

<section class="contact-card abs">
  <svg class="abs" style="left:24px;top:28px" width="34" height="24" viewBox="0 0 34 24"><rect x="1" y="1" width="32" height="22" fill="none" stroke="#4d6d72" stroke-width="2"/><path d="M1 1l16 13L33 1M1 23l12-11M33 23L21 12" fill="none" stroke="#4d6d72" stroke-width="2"/></svg>
  <h2 class="section-title bebas abs" style="left:66px;top:24px;font-size:33px">Get in Touch</h2>
  <div class="field" style="left:24px;top:68px;width:160px;height:22px">Name</div>
  <div class="field" style="left:24px;top:95px;width:160px;height:22px">Email</div>
  <div class="field" style="left:24px;top:121px;width:160px;height:23px">Phone</div>
  <div class="field" style="left:188px;top:68px;width:151px;height:76px">Comments</div>
</section>
<div class="submit abs bebas">Submit</div>

<div class="dotted" style="top:772px;border-top-color:#262626"></div>

<section class="welcome">
  <h2 class="section-title bebas abs" style="left:188px;top:806px;font-size:31px">Welcome to Quenlow</h2>
  <svg class="abs" style="left:188px;top:852px" width="374" height="7" viewBox="0 0 374 7"><path d="M0 1.5H16l4 4 4-4H374" fill="none" stroke="#fff" stroke-width="1.4"/></svg>
  <p class="body-copy abs">Lorem ipsum dolor sit amet, consectetur adipiscing elit. In fermentum dolor non augue pretium egestas. Donec sem eros, tincidunt at congue ut, posuere sit amet est. Vivamus scelerisque viverra odio sit amet laoreet. Ut nec neque non justo rutrum tempor lobortis eu ante. dolor Aliquam sagittis, nibh quis commodo auctor, risus nibh mauris laoreet lectus, id facilisis libero odio nec enim. Sed id ligula adipiscing purus lacinia aliquet. Sed eu est non nisl vehicula bibendum congue sit amet enim.</p>
  <div class="btn abs" style="left:475px;top:994px;width:79px;height:15px">Learn More</div>
</section>

<section class="news">
  <h2 class="section-title bebas abs" style="left:594px;top:806px;font-size:31px">Blog and News</h2>
  <div class="news-thumb abs" style="left:597px;top:851px;background:linear-gradient(135deg,#d9dfe6,#b68aa0)" role="img" aria-label="Photo of a medical consultation"></div>
  <div class="abs" style="left:650px;top:848px">
    <div class="news-date">05 Dec, 2013</div>
    <div class="news-text">Lorem ipsum dolor sit amet, consectetur<br>adipiscing &nbsp;elit. In fermentum congu<br>sit amet, consectetur...</div>
  </div>
  <div class="news-thumb abs" style="left:597px;top:914px;background:linear-gradient(135deg,#e4e8ec,#4a5260)" role="img" aria-label="Photo of business people meeting"></div>
  <div class="abs" style="left:650px;top:911px">
    <div class="news-date">05 Dec, 2013</div>
    <div class="news-text">Lorem ipsum dolor sit amet, consectetur<br>adipiscing &nbsp;elit. In fermentum congu<br>sit amet, consectetur...</div>
  </div>
  <div class="btn abs" style="left:786px;top:994px;width:61px;height:15px">Read All</div>
</section>

<footer class="footer">
  <nav class="footer-nav">
    <span>Home</span><span>Our Prectices</span><span>Professionals</span><span>Careers</span><span>About us</span><span>Contact</span>
  </nav>
  <div class="phone-line abs" style="left:426px;top:58px">
    <span class="phone-icon"><svg width="11" height="11" viewBox="0 0 12 12"><rect x="3" y="1" width="6" height="3" fill="#fff"/><rect x="1" y="4" width="10" height="5" rx="1" fill="#fff"/><rect x="3" y="7" width="6" height="4" fill="#fff" stroke="#4d6d72" stroke-width=".8"/></svg></span>
    <span class="phone-number bebas" style="font-size:24px">555.730.4158</span>
  </div>
  <div class="abs" style="left:0;width:1035px;top:88px;text-align:center;font-size:9.6px;color:#fff">© Copyright 2014</div>
</footer>

</body>
</html>
```